Scent Marketing Solutions by Vapolinth

We need to create 12 page brochure (including the cover and back page) for our Scent Marketing line of products.

The brochure size is 18 cm x 18 cm.

Our competitors are www.breeze-olfa.example and www.nosquell.example
Updates

Hi Designers, 

The budget for this project has been increased to $300. This is a 12 page brochure of size 18cm x 18cm.

Thank you.

Hi all designers,

I uploaded a new brochure draft with the write up in pdf.
I understand that some of you could not open the original file in powerpoint.

Thank you.

Hi Designers,

I added the brochure write up in Word and PDF format. I understand some of you have troubles with it in the earlier files uploaded.

Thank you.

Target Market(s)

B2B audience, such as visual merchandisers of retail brands, hotel managers, real estate property managers etc.

Industry/Entity Type

Marketing

Requirements
Must have
• Our corporate identity uses a lot of white, hence this must be reflected in the brochure.
Our products are high-tech and environmentally friendly, so this must again be reflected in the design.
We want to make the brochure attractive and easy to read, hence would like to allocate more space for photos and pictures and keep the brochure as spacious as possible.
Nice to have
• Since the product is related to the air (it scents the air), we would like to have a design feature that reflects this and is repeated throughout the brochure. It can be a pattern or logo.
Should not have
• Avoid using a lot of bright colors

```html
<!DOCTYPE html>
<html lang="en">
<head>
<meta charset="utf-8">
<title>Vapolinth – Scent Library</title>
<link rel="stylesheet" href="https://fonts.googleapis.com/css2?family=Tinos:ital,wght@0,400;0,700;1,700&display=swap">
<style>
  :root {
    --page-bg: #ffffff;
    --ink: #111111;
    --photo-light: #f4f3f6;
    --photo-mid: #e6e4ea;
    --photo-warm: #f2d9cc;
    --photo-accent: #d43a5c;
  }
  * { margin: 0; padding: 0; box-sizing: border-box; }
  html, body {
    width: 1200px;
    height: 1200px;
    overflow: hidden;
    background: var(--page-bg);
  }
  .page {
    position: relative;
    width: 1200px;
    height: 1200px;
    background: var(--page-bg);
    font-family: "Tinos", "Times New Roman", serif;
    color: var(--ink);
  }
  .hero-photo {
    position: absolute;
    left: 0;
    top: 0;
    width: 1200px;
    height: 333px;
    background:
      radial-gradient(ellipse at 22% 45%, var(--photo-warm) 0%, rgba(242,217,204,0) 38%),
      linear-gradient(160deg, var(--photo-light) 0%, var(--photo-mid) 55%, #f0e2e6 100%);
  }
  .hero-photo::after {
    content: "";
    position: absolute;
    inset: 0;
    background: radial-gradient(ellipse at 70% 40%, rgba(212,58,92,0.18) 0%, rgba(212,58,92,0) 60%);
  }
  .intro {
    position: absolute;
    left: 82px;
    top: 331px;
    width: 1060px;
    font-size: 37px;
    line-height: 50px;
  }
  .intro .line { display: block; white-space: nowrap; }
  .scent-list {
    position: absolute;
    left: 86px;
    top: 777px;
    list-style: none;
    font-size: 37px;
    line-height: 52px;
    font-weight: 700;
    font-style: italic;
  }
  .scent-list li {
    position: relative;
    padding-left: 52px;
    white-space: nowrap;
  }
  .scent-list li::before {
    content: "";
    position: absolute;
    left: 0;
    top: 22px;
    width: 10px;
    height: 10px;
    border-radius: 50%;
    background: var(--ink);
  }
</style>
</head>
<body>
  <main class="page">
    <div class="hero-photo" role="img" aria-label="Photograph of a pale festive bauble resting on white with loose red ribbon curls"></div>

    <p class="intro">
      <span class="line">With our extensive library of more than 1,000 different</span>
      <span class="line">scents and our capabilities to design signature scents ex–</span>
      <span class="line">clusively for you brand, finding the right scent for your</span>
      <span class="line">business is easy. The right scent can draw customers into</span>
      <span class="line">your premises, make them stay longer, and create a sub–</span>
      <span class="line">conscious bond that makes clistomers think of you every</span>
      <span class="line">time they experience your unique scent.</span>
      <span class="line">Vapolinth has all types of scents, including:</span>
    </p>

    <ul class="scent-list">
      <li>Signature scents</li>
      <li>Mood influencing scents (e.g. calming, uplifting etc)</li>
      <li>Festive scents (e.g. Christmas, New Year, etc.)</li>
      <li>Themed scents (e.g. beach, gardent, etc.)</li>
      <li>Product scents (e.g. coffee, popcorn etc.)</li>
    </ul>
  </main>
</body>
</html>
```